Business Card Design needed for start up company Pelmora

In need of a new business card designed for a start up company based in Sydney, Pelmora is a new start up innovative Company, our mission it to make property accessible for everyday Australian and to become the leading Real Estate platform in Australia. We want it to be fresh and clean.

Industry/Entity Type

Financial

Contact Information for Business Card

Section for Name
Section for Title

PELMORA - Keys Within Reach
Mobile:
Direct:

Font styles to use
Sans Serif

Colors
33a6d7
0692cd
0255a3
ffffff

Requirements
Must have
• Logo, all business card details

```html
<!DOCTYPE html>
<html lang="en">
<head>
<meta charset="utf-8">
<title>Pelmora Business Card</title>
<link href="https://fonts.googleapis.com/css2?family=Roboto:wght@400;500;700&display=swap" rel="stylesheet">
<style>
  :root {
    --page: #d6d6d6;
    --white: #ffffff;
    --paper-top: #fafafa;
    --paper-bottom: #d4d4d4;
    --sky: #33a6d7;
    --blue: #0692cd;
    --blue-deep: #0a6aaa;
    --navy: #0255a3;
    --navy-top: #1f4a7e;
    --navy-bottom: #1a3966;
    --ink: #1d4a82;
    --soft-text: #dceaf6;
  }
  * { box-sizing: border-box; margin: 0; padding: 0; }
  html, body { width: 1200px; height: 965px; overflow: hidden; }
  body {
    background: var(--page);
    font-family: "Roboto", Arial, sans-serif;
    position: relative;
  }
  .card {
    position: absolute;
    left: 277px;
    width: 648px;
    height: 368px;
    overflow: hidden;
  }
  .card-front { top: 98px; }
  .card-back {
    top: 502px;
    background: linear-gradient(180deg, var(--navy-top), var(--navy-bottom));
  }

  /* Front */
  .front-brand {
    position: absolute; left: 0; top: 0; width: 328px; height: 100%;
    background: linear-gradient(180deg, var(--paper-top) 0%, #f1f1f1 50%, var(--paper-bottom) 100%);
  }
  .front-details {
    position: absolute; left: 328px; top: 0; right: 0; height: 100%;
    background: linear-gradient(180deg, #0f7cc4, var(--blue-deep));
  }
  .notch { position: absolute; left: 328px; top: 58px; }
  .wordmark {
    position: absolute; display: flex; align-items: center;
  }
  .wordmark-front { left: 20px; top: 142px; gap: 8px; }
  .wordmark-dot { border-radius: 50%; flex: none; }
  .wordmark-front .wordmark-dot { width: 84px; height: 84px; background: #2293cf; }
  .wordmark-name { font-weight: 700; line-height: 1; }
  .wordmark-front .wordmark-name { font-size: 35px; color: var(--ink); letter-spacing: -0.5px; }

  .person { position: absolute; left: 382px; top: 62px; color: var(--white); }
  .person-name { font-size: 26px; font-weight: 700; letter-spacing: 0.2px; line-height: 1.1; }
  .person-title { font-size: 19px; font-weight: 400; margin-top: 2px; }

  .contact-list { position: absolute; left: 384px; top: 152px; list-style: none; }
  .contact-list li {
    display: flex; align-items: center; gap: 8px;
    height: 21.6px; font-size: 17.5px; color: var(--white);
  }
  .contact-list svg { width: 15px; height: 15px; flex: none; }
  .address {
    position: absolute; left: 382px; top: 266px;
    font-size: 17.5px; line-height: 22px; color: var(--soft-text);
    font-style: normal;
  }

  /* Back */
  .wordmark-back { left: 88px; top: 114px; gap: 14px; }
  .wordmark-back .wordmark-dot { width: 144px; height: 144px; background: var(--white); }
  .wordmark-back .wordmark-name { font-size: 66px; color: var(--white); letter-spacing: -1px; }
  .tagline {
    position: absolute; left: 233px; top: 236px;
    font-size: 20px; color: var(--white); letter-spacing: 4px;
  }
</style>
</head>
<body>
  <section class="card card-front" aria-label="Card front">
    <div class="front-brand"></div>
    <div class="front-details"></div>
    <svg class="notch" width="29" height="56" viewBox="0 0 29 56" aria-hidden="true">
      <polygon points="0,0 28,28 0,56" fill="#0e78bf"/>
    </svg>
    <div class="wordmark wordmark-front">
      <span class="wordmark-dot"></span>
      <span class="wordmark-name">PELMORA</span>
    </div>
    <div class="person">
      <p class="person-name">CLARA DUNMORE</p>
      <p class="person-title">Managing Director</p>
    </div>
    <ul class="contact-list">
      <li>
        <svg viewBox="0 0 16 16" aria-hidden="true"><rect x="1" y="3" width="4" height="11" fill="#fff"/><rect x="6" y="2" width="9" height="12" fill="none" stroke="#fff" stroke-width="1.5"/><rect x="8" y="4" width="5" height="3" fill="#fff"/></svg>
        +61 2 5550 1842
      </li>
      <li>
        <svg viewBox="0 0 16 16" aria-hidden="true"><rect x="4" y="1" width="8" height="14" rx="1.5" fill="none" stroke="#fff" stroke-width="1.5"/><circle cx="8" cy="12.5" r="0.9" fill="#fff"/></svg>
        +61 455 500 267
      </li>
      <li>
        <svg viewBox="0 0 16 16" aria-hidden="true"><rect x="1" y="4" width="14" height="9" fill="none" stroke="#fff" stroke-width="1.5"/><polyline points="1,4 8,10 15,4" fill="none" stroke="#fff" stroke-width="1.5"/></svg>
        hello@PELMORA.com.au
      </li>
      <li>
        <svg viewBox="0 0 16 16" aria-hidden="true"><circle cx="8" cy="8" r="6.5" fill="none" stroke="#fff" stroke-width="1.2"/><ellipse cx="8" cy="8" rx="3" ry="6.5" fill="none" stroke="#fff" stroke-width="1.2"/><line x1="1.5" y1="8" x2="14.5" y2="8" stroke="#fff" stroke-width="1.2"/></svg>
        www.PELMORA.com.au
      </li>
    </ul>
    <address class="address">Level 4, 112 Harlow Lane,<br>Paddington, NSW, 2021</address>
  </section>

  <section class="card card-back" aria-label="Card back">
    <div class="wordmark wordmark-back">
      <span class="wordmark-dot"></span>
      <span class="wordmark-name">PELMORA</span>
    </div>
    <p class="tagline">Keys Within Reach</p>
  </section>
</body>
</html>
```